DOUBLE SIDED BROCHURE NEEDED TO PROMOTE DOCTOR

I need a double sided DL size (99mm x 210mm) brochure, promoting a doctor seeing patients in a new area.

I want something professional. I have included the relevant information. I would also like the Dr's picture somwhere in the brochure, with a professional background. I wish to print these tomorrow, so i will pick a winner within 14 hours of posting this ad.

I have included an example of a brochures design that I recently saw, and its definietly a good starting point.

Medical

```html
<!DOCTYPE html>
<html lang="en">
<head>
<meta charset="utf-8">
<title>Dr. Samir Haddad – DL Brochure</title>
<link rel="stylesheet" href="https://fonts.googleapis.com/css2?family=Source+Sans+3:wght@400;600;700&family=Open+Sans:wght@600;700&display=swap">
<style>
  :root {
    --blue: #10b0d8;
    --wave-mid: #74cde7;
    --wave-light: #d3f0f8;
    --title-blue: #1f6fb7;
    --ink: #222;
    --paper: #ffffff;
    --footer-grey: #f2f2f2;
    --stage: #e9ecee;
  }
  * { box-sizing: border-box; margin: 0; padding: 0; }
  html, body { width: 1167px; height: 1200px; overflow: hidden; }
  body {
    background: var(--stage);
    font-family: "Source Sans 3", "Myriad Pro", sans-serif;
    position: relative;
  }
  .panel {
    position: absolute;
    top: 125px;
    width: 452px;
    height: 950px;
    background: var(--blue);
    overflow: hidden;
    color: var(--paper);
    box-shadow: 0 4px 14px rgba(0,0,0,.18);
  }
  .panel--front { left: 88px; }
  .panel--back { left: 627px; }
  .panel__waves { position: absolute; left: 0; top: 0; width: 452px; height: 950px; }

  /* Front */
  .portrait {
    position: absolute; left: 0; top: 0; width: 452px; height: 600px;
    background: linear-gradient(180deg, #eef1f4 0%, #d9dee3 55%, #c5cbd1 100%);
  }
  .greeting {
    position: absolute; top: 588px; width: 100%;
    text-align: center; font-size: 27px; font-weight: 400;
  }
  .announcement {
    position: absolute; top: 643px; left: 30px; right: 30px;
    text-align: center; font-size: 15.5px; line-height: 1.32; font-weight: 600;
  }
  .announcement p + p { margin-top: 19px; }
  .referral {
    position: absolute; left: 0; top: 862px; width: 100%; height: 60px;
    background: var(--paper); color: var(--ink);
    text-align: center; font-size: 15.5px; padding-top: 9px;
  }
  .referral__fax {
    display: inline-flex; align-items: center; gap: 8px; margin-top: 3px;
    color: var(--title-blue); font-weight: 700;
  }

  /* Back */
  .header-photo {
    position: absolute; left: 0; top: 0; width: 452px; height: 240px;
    background: linear-gradient(90deg, #f1f4f6 0%, #e4e9ed 60%, #dfe4e8 78%, #f3f3f3 100%);
  }
  .doctor-name {
    position: absolute; top: 96px; left: 92px;
    color: var(--title-blue); font-size: 35px; font-weight: 400;
  }
  .intro {
    position: absolute; top: 262px; left: 36px; right: 28px;
    font-size: 17.5px; line-height: 1.5; text-align: justify;
  }
  .services {
    position: absolute; left: 36px; list-style: none;
    font-size: 18.5px; line-height: 1.43;
  }
  .services--specialist { top: 360px; }
  .services--general { top: 636px; }
  .services li { display: flex; align-items: center; gap: 9px; }
  .services svg { flex: none; }
  .divider {
    position: absolute; top: 537px; left: 60px; width: 332px; height: 1px;
    background: linear-gradient(90deg, rgba(255,255,255,0), #fff 15%, #fff 85%, rgba(255,255,255,0));
  }
  .general-lead {
    position: absolute; top: 596px; left: 30px; font-size: 18px;
  }
  .clinic {
    position: absolute; left: 0; top: 845px; width: 100%;
    text-align: center; color: var(--ink);
    font-family: "Open Sans", "Segoe UI", sans-serif;
  }
  .clinic__name { font-size: 13.5px; font-weight: 700; }
  .clinic__phone {
    display: inline-flex; align-items: center; gap: 10px;
    font-size: 18px; font-weight: 700; margin-top: 4px;
  }
  .clinic__address { font-size: 12.5px; font-weight: 600; margin-top: 3px; }
  .clinic__web { font-size: 14px; font-weight: 700; color: var(--title-blue); margin-top: 6px; letter-spacing: .4px; }
</style>
</head>
<body>

<section class="panel panel--front">
  <div class="portrait" role="img" aria-label="Portrait photo of the doctor in a dark jacket against a softly blurred clinic background"></div>
  <svg class="panel__waves" viewBox="0 0 452 950" aria-hidden="true">
    <path d="M0,478 C160,522 340,462 452,372 L452,620 L0,620 Z" fill="var(--wave-light)"/>
    <path d="M0,496 C170,540 350,482 452,398 L452,620 L0,620 Z" fill="var(--wave-mid)"/>
    <path d="M0,514 C180,560 360,506 452,424 L452,620 L0,620 Z" fill="var(--blue)"/>
  </svg>
  <h2 class="greeting">Dear Doctors,</h2>
  <div class="announcement">
    <p>We are pleased to announce that Dr. Samir Haddad<br>is now consulting in Seaside, seeing<br>public and private patients.</p>
    <p>Guaranteed appointment within two weeks, with<br>patients having the option of surgery at Coastal Health<br>Campus, Harbourview Hospital or<br>St. Clare Private Hospital.</p>
  </div>
  <div class="referral">
    Please send all referrals by fax to<br>
    <span class="referral__fax">
      <svg width="14" height="14" viewBox="0 0 14 14" aria-hidden="true">
        <rect x="3" y="1" width="8" height="4" fill="none" stroke="var(--title-blue)" stroke-width="1.5"/>
        <rect x="1" y="5" width="12" height="6" rx="1" fill="var(--title-blue)"/>
        <rect x="3.5" y="9" width="7" height="4" fill="#fff" stroke="var(--title-blue)" stroke-width="1.2"/>
      </svg>
      (08) 5550 7143
    </span>
  </div>
</section>

<section class="panel panel--back">
  <div class="header-photo" role="img" aria-label="Photo of a doctor in a white coat with a stethoscope, arms folded, cropped at the shoulders"></div>
  <svg class="panel__waves" viewBox="0 0 452 950" aria-hidden="true">
    <path d="M0,132 C120,190 330,200 452,140 L452,260 L0,260 Z" fill="var(--wave-light)"/>
    <path d="M0,148 C120,206 330,214 452,158 L452,260 L0,260 Z" fill="var(--wave-mid)"/>
    <path d="M0,162 C120,222 330,228 452,174 L452,260 L0,260 Z" fill="var(--blue)"/>
    <path d="M0,835 C140,772 310,772 452,832 L452,950 L0,950 Z" fill="var(--wave-mid)"/>
    <path d="M0,858 C140,792 310,792 452,856 L452,950 L0,950 Z" fill="var(--footer-grey)"/>
  </svg>
  <h1 class="doctor-name">Dr. Samir Haddad</h1>
  <p class="intro">Dr. Haddad is a highly trained specialised surgeon, in all areas of Endocrine, Breast and General Surgery. Including;</p>
  <ul class="services services--specialist">
    <li><svg width="14" height="14" viewBox="0 0 14 14" aria-hidden="true"><circle cx="7" cy="7" r="7" fill="#fff"/><path d="M5.5,4 L8.5,7 L5.5,10" fill="none" stroke="var(--blue)" stroke-width="1.8"/></svg>Thyroid Surgery</li>
    <li><svg width="14" height="14" viewBox="0 0 14 14" aria-hidden="true"><circle cx="7" cy="7" r="7" fill="#fff"/><path d="M5.5,4 L8.5,7 L5.5,10" fill="none" stroke="var(--blue)" stroke-width="1.8"/></svg>Parathyroid surgery (including minimally</li>
    <li><svg width="14" height="14" viewBox="0 0 14 14" aria-hidden="true"><circle cx="7" cy="7" r="7" fill="#fff"/><path d="M5.5,4 L8.5,7 L5.5,10" fill="none" stroke="var(--blue)" stroke-width="1.8"/></svg>invasive parathyroidectomy)</li>
    <li><svg width="14" height="14" viewBox="0 0 14 14" aria-hidden="true"><circle cx="7" cy="7" r="7" fill="#fff"/><path d="M5.5,4 L8.5,7 L5.5,10" fill="none" stroke="var(--blue)" stroke-width="1.8"/></svg>Breast Cancer</li>
    <li><svg width="14" height="14" viewBox="0 0 14 14" aria-hidden="true"><circle cx="7" cy="7" r="7" fill="#fff"/><path d="M5.5,4 L8.5,7 L5.5,10" fill="none" stroke="var(--blue)" stroke-width="1.8"/></svg>Benign breast lesions</li>
  </ul>
  <div class="divider"></div>
  <p class="general-lead">All areas of general surgery, such as;</p>
  <ul class="services services--general">
    <li><svg width="14" height="14" viewBox="0 0 14 14" aria-hidden="true"><circle cx="7" cy="7" r="7" fill="#fff"/><path d="M5.5,4 L8.5,7 L5.5,10" fill="none" stroke="var(--blue)" stroke-width="1.8"/></svg>Gallbladder surgery</li>
    <li><svg width="14" height="14" viewBox="0 0 14 14" aria-hidden="true"><circle cx="7" cy="7" r="7" fill="#fff"/><path d="M5.5,4 L8.5,7 L5.5,10" fill="none" stroke="var(--blue)" stroke-width="1.8"/></svg>Hernia surgery</li>
    <li><svg width="14" height="14" viewBox="0 0 14 14" aria-hidden="true"><circle cx="7" cy="7" r="7" fill="#fff"/><path d="M5.5,4 L8.5,7 L5.5,10" fill="none" stroke="var(--blue)" stroke-width="1.8"/></svg>Haemorrhoids</li>
    <li><svg width="14" height="14" viewBox="0 0 14 14" aria-hidden="true"><circle cx="7" cy="7" r="7" fill="#fff"/><path d="M5.5,4 L8.5,7 L5.5,10" fill="none" stroke="var(--blue)" stroke-width="1.8"/></svg>Carpal Tunnel</li>
    <li><svg width="14" height="14" viewBox="0 0 14 14" aria-hidden="true"><circle cx="7" cy="7" r="7" fill="#fff"/><path d="M5.5,4 L8.5,7 L5.5,10" fill="none" stroke="var(--blue)" stroke-width="1.8"/></svg>Vasectomy etc etc…</li>
  </ul>
  <div class="clinic">
    <div class="clinic__name">Seaside Clinic</div>
    <div class="clinic__phone">
      <svg width="20" height="20" viewBox="0 0 20 20" aria-hidden="true">
        <circle cx="10" cy="10" r="8.8" fill="none" stroke="var(--ink)" stroke-width="1.5"/>
        <path d="M7,5.2 L8.6,7.6 L7.6,8.8 C8.3,10.3 9.6,11.6 11.2,12.4 L12.4,11.4 L14.8,13 L13.8,14.6 C10,14.6 5.4,10 5.4,6.2 Z" fill="var(--ink)"/>
      </svg>
      1300 555 018
    </div>
    <div class="clinic__address">42 Marina Parade Seaside WA 6000.</div>
    <div class="clinic__web">www.seasideclinic.example</div>
  </div>
</section>

</body>
</html>
```